Business Card Design

I would like a new business card design for an accounting firm that specializes in resolving clients tax problems. I want the card to give the impression that we are not your typical stodgy accounting firm, but at the same time we will get the job done.
Industry/Entity Type
Business
Contact Information for Business Card
Dorian T Welsby
Certified Public Accountant
38-27 52nd Street
Sunnyside, NY 11287
Tel: (718) 555-0142
Fax: (888) 555-0199
e-mail: dtwthecpa@ledgerpost.com
website: harborfilingreliefexperts.com

```html
<!DOCTYPE html>
<html lang="en">
<head>
<meta charset="utf-8">
<title>Dorian T Welsby – Business Card</title>
<link rel="stylesheet" href="https://fonts.googleapis.com/css2?family=Fira+Sans:wght@400;600&family=Oswald:wght@600&display=swap">
<style>
  :root {
    --navy: #1f3a52;
    --green: #7ce11c;
    --ink: #2b3f55;
    --paper: #ffffff;
  }
  * { margin: 0; padding: 0; box-sizing: border-box; }
  html, body { width: 1200px; height: 693px; overflow: hidden; background: var(--paper); }
  .card {
    position: relative;
    width: 1200px;
    height: 693px;
    background: var(--paper);
    font-family: "Fira Sans", Arial, sans-serif;
    color: var(--ink);
  }
  .band { position: absolute; display: block; }
  .band-top { left: 34px; top: 34px; }
  .band-bottom { left: 592px; top: 634px; }

  .brand {
    position: absolute;
    left: 200px;
    top: 420px;
    width: 310px;
    display: flex;
    align-items: center;
    justify-content: center;
    gap: 16px;
  }
  .brand-square { width: 40px; height: 40px; background: var(--green); flex: none; }
  .brand-name {
    font-family: "Fira Sans", Arial, sans-serif;
    font-weight: 600;
    font-size: 48px;
    color: var(--navy);
    letter-spacing: 0.5px;
    white-space: nowrap;
  }

  .divider {
    position: absolute;
    left: 608px;
    top: 219px;
    width: 3px;
    height: 343px;
    background: var(--green);
  }

  .identity {
    position: absolute;
    left: 630px;
    top: 222px;
    width: 470px;
    text-align: center;
  }
  .name {
    display: inline-block;
    font-weight: 600;
    font-size: 61px;
    line-height: 1;
    color: var(--navy);
    padding: 0 10px 6px;
    border-bottom: 3px solid var(--green);
    white-space: nowrap;
  }
  .title, .address {
    font-size: 24px;
    line-height: 32px;
    color: var(--ink);
    white-space: nowrap;
  }
  .title { margin-top: 4px; }

  .contacts {
    position: absolute;
    left: 635px;
    top: 379px;
    list-style: none;
  }
  .contact {
    display: flex;
    align-items: center;
    gap: 14px;
    height: 32px;
    margin-bottom: 15px;
    font-size: 24px;
    color: var(--ink);
    white-space: nowrap;
  }
  .contact-icon { width: 32px; height: 32px; flex: none; }
</style>
</head>
<body>
<main class="card">
  <svg class="band band-top" width="600" height="25" viewBox="0 0 600 25" aria-hidden="true">
    <polygon points="0,0 600,0 583,25 0,25" fill="var(--navy)"/>
  </svg>
  <svg class="band band-bottom" width="588" height="25" viewBox="0 0 588 25" aria-hidden="true">
    <polygon points="17,0 588,0 588,25 0,25" fill="var(--navy)"/>
  </svg>

  <div class="brand">
    <span class="brand-square"></span>
    <span class="brand-name">WELSBY TAX</span>
  </div>

  <div class="divider"></div>

  <section class="identity">
    <h1 class="name">Dorian T Welsby</h1>
    <p class="title">Certified Public Accountant</p>
    <p class="address">38-27 52nd Street Sunnyside, NY 11287</p>
  </section>

  <ul class="contacts">
    <li class="contact">
      <svg class="contact-icon" viewBox="0 0 32 32" aria-hidden="true">
        <circle cx="16" cy="16" r="16" fill="var(--green)"/>
        <path d="M10.5 8.5c1-.6 2-.4 2.6.5l1.6 2.6c.5.8.3 1.7-.4 2.2l-1.1.8c.8 1.8 2.4 3.5 4.3 4.4l.8-1.1c.5-.7 1.5-.9 2.2-.4l2.6 1.6c.9.6 1.1 1.6.5 2.6-.9 1.6-2.6 2.3-4.4 1.7-4.4-1.4-8-5-9.4-9.4-.6-1.8.1-3.5 1.7-4.4z" fill="#fff"/>
      </svg>
      <span>Tel: (718) 555-0142</span>
    </li>
    <li class="contact">
      <svg class="contact-icon" viewBox="0 0 32 32" aria-hidden="true">
        <circle cx="16" cy="16" r="16" fill="var(--green)"/>
        <path d="M10.5 8.5c1-.6 2-.4 2.6.5l1.6 2.6c.5.8.3 1.7-.4 2.2l-1.1.8c.8 1.8 2.4 3.5 4.3 4.4l.8-1.1c.5-.7 1.5-.9 2.2-.4l2.6 1.6c.9.6 1.1 1.6.5 2.6-.9 1.6-2.6 2.3-4.4 1.7-4.4-1.4-8-5-9.4-9.4-.6-1.8.1-3.5 1.7-4.4z" fill="#fff"/>
      </svg>
      <span>Fax: (888) 555-0199</span>
    </li>
    <li class="contact">
      <svg class="contact-icon" viewBox="0 0 32 32" aria-hidden="true">
        <circle cx="16" cy="16" r="16" fill="var(--green)"/>
        <rect x="8" y="10.5" width="16" height="11" fill="#fff"/>
        <polyline points="8,10.5 16,17 24,10.5" fill="none" stroke="var(--green)" stroke-width="1.6"/>
      </svg>
      <span>dtwthecpa@ledgerpost.com</span>
    </li>
    <li class="contact">
      <svg class="contact-icon" viewBox="0 0 32 32" aria-hidden="true">
        <circle cx="16" cy="16" r="16" fill="var(--green)"/>
        <g fill="none" stroke="#fff" stroke-width="1.5">
          <circle cx="16" cy="16" r="8.5"/>
          <ellipse cx="16" cy="16" rx="3.8" ry="8.5"/>
          <line x1="7.5" y1="16" x2="24.5" y2="16"/>
          <line x1="9" y1="11.5" x2="23" y2="11.5"/>
          <line x1="9" y1="20.5" x2="23" y2="20.5"/>
        </g>
      </svg>
      <span>www.harborfilingreliefexperts.com</span>
    </li>
  </ul>
</main>
</body>
</html>
```